Business Card Design

Company name is: Tallowmere Rescue Skills, LLC. We teach CPR/AED, First Aid, Bloodborne Pathogens and other health and safety classes. Looking for an eye-catching, progressive, cutting edge design.

Industry/Entity Type

Health

Contact Information for Business Card

Dale Fenwarick (555.218.4703)
Nora Quillstead (555.276.9148)
email is info@tallowmererescue.example
website is www.TallowmereRescue.example

```html
<!DOCTYPE html>
<html lang="en">
<head>
<meta charset="utf-8">
<title>Tallowmere Rescue Skills, LLC – Business Card</title>
<link href="https://fonts.googleapis.com/css2?family=Mulish:wght@400;700&display=swap" rel="stylesheet">
<style>
  :root {
    --backdrop: #ece9e4;
    --card: #ffffff;
    --green-dark: #1c5e2c;
    --green: #2e8a3e;
    --green-soft: #4da058;
    --ink: #1a1a1a;
    --faint: #e8ece8;
    --faint-fill: #f2f5f2;
  }
  * { margin: 0; padding: 0; box-sizing: border-box; }
  html, body {
    width: 1200px; height: 1000px; overflow: hidden;
    background: var(--backdrop);
    font-family: "Mulish", sans-serif;
  }
  .business-card {
    position: absolute; left: 67px; top: 181px;
    width: 1066px; height: 637px;
    background: var(--card);
    box-shadow: 0 6px 18px rgba(0,0,0,0.18);
    overflow: hidden;
  }
  .brand {
    position: absolute; left: 51px; top: 54px;
    display: flex; align-items: center; gap: 28px;
  }
  .brand-disc {
    width: 166px; height: 160px; border-radius: 50%;
    background: radial-gradient(circle at 40% 35%, var(--green-soft), var(--green-dark));
    flex: none;
  }
  .brand-name {
    font-weight: 700; font-size: 46px; line-height: 1.08;
    color: var(--green);
  }
  .backdrop-disc {
    position: absolute; left: 568px; top: 139px;
    width: 480px; height: 480px; border-radius: 50%;
    background: var(--faint-fill);
    border: 10px solid var(--faint);
  }
  .contacts { position: absolute; left: 51px; top: 306px; }
  .person { margin-bottom: 22px; }
  .person-name {
    font-weight: 700; font-size: 32px; color: var(--green-dark); line-height: 1.2;
  }
  .contact-line {
    display: flex; align-items: center; gap: 8px;
    font-size: 26px; color: var(--ink); line-height: 1.45;
  }
  .contact-line svg { width: 20px; height: 20px; flex: none; fill: var(--green-dark); }
  .web-links { margin-top: 30px; }
</style>
</head>
<body>
  <section class="business-card">
    <div class="backdrop-disc" role="img" aria-label="Large faint emblem area"></div>

    <header class="brand">
      <div class="brand-disc" aria-hidden="true"></div>
      <h1 class="brand-name">Tallowmere Rescue<br>Skills, LLC</h1>
    </header>

    <div class="contacts">
      <div class="person">
        <p class="person-name">Dale Fenwarick</p>
        <p class="contact-line">
          <svg viewBox="0 0 20 20" aria-hidden="true"><path d="M5 2c1 0 2 3 2 4s-2 1-1 3 3 4 5 5 2-1 3-1 4 1 4 2-2 3-3 3C9 18 2 11 2 5c0-1 2-3 3-3z"/></svg>
          (555.218.4703)
        </p>
      </div>
      <div class="person">
        <p class="person-name">Nora Quillstead</p>
        <p class="contact-line">
          <svg viewBox="0 0 20 20" aria-hidden="true"><path d="M5 2c1 0 2 3 2 4s-2 1-1 3 3 4 5 5 2-1 3-1 4 1 4 2-2 3-3 3C9 18 2 11 2 5c0-1 2-3 3-3z"/></svg>
          (555.276.9148)
        </p>
      </div>
      <div class="web-links">
        <p class="contact-line">
          <svg viewBox="0 0 20 20" aria-hidden="true"><path d="M1 4h18v12H1z"/><path d="M1 4l9 7 9-7" fill="none" stroke="#fff" stroke-width="1.6"/></svg>
          info@tallowmererescue.example
        </p>
        <p class="contact-line">
          <svg viewBox="0 0 20 20" aria-hidden="true"><circle cx="10" cy="10" r="9"/><g fill="none" stroke="#fff" stroke-width="1.2"><ellipse cx="10" cy="10" rx="4" ry="9"/><path d="M1 10h18M2.5 5.5h15M2.5 14.5h15M10 1v18"/></g></svg>
          www.TallowmereRescue.example
        </p>
      </div>
    </div>
  </section>
</body>
</html>
```